USB Flash Drive Catalogue

I would like to make a paper catalogue of the products from our Quorvel store. There are currently 209 items on Quorvel. Some would be excluded. The listings have pricing and would need to be organized a bit different but all the information is there.

https://www.quorvel.com/shop/BrightPinStock/items?ref=pagination&page=1

Store

```html
<!DOCTYPE html>
<html lang="en">
<head>
<meta charset="utf-8">
<title>BrightPinStock Catalog – Pages 3–4</title>
<link rel="stylesheet" href="https://fonts.googleapis.com/css2?family=PT+Sans:wght@400;700&family=PT+Sans+Narrow:wght@400;700&display=swap">
<style>
:root{
  --orange:#d98a3c;
  --bar:#3e3e40;
  --ink:#3a3a3a;
  --muted:#6b6b6b;
  --paper:#ffffff;
  --backdrop:#e4e3df;
  --maple:#ece7df;
  --maple-deep:#c9b79a;
  --walnut:#6b4a35;
  --walnut-deep:#3f2a1d;
  --pine:#e6cf9c;
}
*{box-sizing:border-box;margin:0;padding:0}
html,body{width:1200px;height:804px;overflow:hidden}
body{background:var(--backdrop);font-family:"PT Sans",sans-serif;color:var(--ink)}
.spread{position:absolute;left:14px;top:12px;width:1172px;height:780px;display:flex;box-shadow:0 4px 18px rgba(0,0,0,.18)}
.page{position:relative;width:586px;height:780px;background:var(--paper);overflow:hidden}
.page--left{border-right:1px solid #dcdcdc}

.page-head{position:absolute;top:0;left:0;right:0;height:56px}
.head-band{position:absolute;top:14px;height:30px;background:var(--orange);color:#fff;font-size:10.5px;line-height:30px;padding:0 24px;white-space:nowrap}
.page--left .head-band{left:0;width:270px;clip-path:polygon(0 0,92% 0,100% 100%,0 100%)}
.page--right .head-band{right:0;width:270px;text-align:right;clip-path:polygon(8% 0,100% 0,100% 100%,0 100%)}
.head-rule{position:absolute;top:46px;left:0;right:0;height:3px;background:linear-gradient(#9c9c9c,#d0d0d0)}
.brand{position:absolute;top:20px;display:flex;align-items:center;gap:6px;font-weight:700;font-size:11px;letter-spacing:1.5px;color:#444}
.brand-dot{width:10px;height:10px;border-radius:50%;background:var(--orange)}
.page--left .brand{right:24px}
.page--right .brand{left:24px}

.catalog-grid{position:absolute;top:62px;left:30px;right:30px;bottom:58px;display:grid;grid-template-columns:1fr 1fr;grid-template-rows:repeat(3,1fr);column-gap:34px}
.item{display:flex;flex-direction:column;align-items:stretch}
.photo{align-self:center;width:130px;height:96px;border-radius:4px;margin:4px 0 6px}
.photo--maple{background:linear-gradient(160deg,var(--maple) 45%,var(--maple-deep))}
.photo--walnut{background:linear-gradient(160deg,var(--walnut) 40%,var(--walnut-deep))}
.photo--pine{background:linear-gradient(160deg,var(--pine) 45%,#c9a666)}
.title-row{display:flex;align-items:flex-end;justify-content:space-between;border-bottom:1px solid var(--orange);padding-bottom:2px}
.title-row h3{font-family:"PT Sans Narrow",sans-serif;font-weight:700;font-size:15px;color:#3b3b3b;white-space:nowrap}
.tag{display:flex;flex-direction:column;align-items:flex-end}
.cap{font-family:"PT Sans Narrow",sans-serif;font-weight:700;font-size:12px;color:var(--orange);line-height:1}
.price{background:var(--orange);color:#fff;font-weight:700;font-size:12px;padding:1px 6px;margin-top:2px}
.specs{list-style:none;margin-top:4px;font-size:7.6px;line-height:1.3;color:var(--muted)}
.specs li{margin-bottom:4px}
.specs b{display:block;color:#444;font-weight:700}
.specs span{display:block;padding-left:10px}
.specs .lead{color:#555;font-size:8px}

.page-foot{position:absolute;left:0;right:0;bottom:0;height:50px}
.foot-bar{position:absolute;top:12px;height:30px;background:var(--bar);color:#eee;font-size:9.5px;line-height:30px;text-align:center}
.foot-tab{position:absolute;top:10px;height:40px;width:150px;background:var(--orange);color:#fff;font-size:10px;line-height:40px;text-align:center}
.page-num{position:absolute;top:4px;width:20px;height:20px;border-radius:50%;background:var(--paper);border:3px solid var(--orange);font-size:9px;font-weight:700;line-height:14px;text-align:center;color:#333}
.page--left .foot-tab{left:0}
.page--left .foot-bar{left:158px;right:0}
.page--left .page-num{right:30px}
.page--right .foot-tab{right:0}
.page--right .foot-bar{left:0;right:158px}
.page--right .page-num{left:30px}
</style>
</head>
<body>
<main class="spread">

  <section class="page page--left">
    <header class="page-head">
      <div class="head-band">USA Company Based in Larkfield, OH</div>
      <div class="brand"><span class="brand-dot"></span>BrightPinStock</div>
      <div class="head-rule"></div>
    </header>

    <div class="catalog-grid">
      <article class="item">
        <div class="photo photo--maple" role="img" aria-label="White maple box with engraved lid and USB drive on raffia"></div>
        <div class="title-row"><h3>Antique Maple Wood</h3><div class="tag"><span class="cap">16 GB</span><span class="price">$ 25.95</span></div></div>
        <ul class="specs">
          <li><b>(1) Laser Engraved Maple wooden box filled Raffia grass.</b><span>Approximate dimensions: 104 x 96 x 39mm</span></li>
          <li><b>(1) 16GB maple wood USB drive, Wildwood Body, painted in Wedding White.</b><span>Approximate dimensions: 60 x 28 x 10mm</span></li>
        </ul>
      </article>
      <article class="item">
        <div class="photo photo--maple" role="img" aria-label="White maple box with engraved lid and heart USB drive"></div>
        <div class="title-row"><h3>Antique Maple Wood</h3><div class="tag"><span class="cap">16 GB</span><span class="price">$ 21.95</span></div></div>
        <ul class="specs">
          <li><b>(1) Laser Engraved Maple wooden box filled Raffia grass.</b><span>Approximate dimensions: 104 x 96 x 39mm</span></li>
          <li><b>(1) maple wood USB drive, painted in Wedding White.</b><span>Approximate dimensions: 60 x 28 x 10mm</span></li>
        </ul>
      </article>
      <article class="item">
        <div class="photo photo--walnut" role="img" aria-label="Engraved walnut box with walnut USB drive"></div>
        <div class="title-row"><h3>Walnut Wood Flash Drive</h3><div class="tag"><span class="cap">8GB/16GB</span><span class="price">$ 22.95</span></div></div>
        <ul class="specs">
          <li><b>(1) Laser Engraved Walnut wooden box filled Raffia grass.</b><span>Approximate dimensions: 104 x 96 x 39mm</span></li>
          <li><b>(1) Walnut wood USB drive</b><span>Approximate dimensions: 60 x 28 x 10mm</span></li>
        </ul>
      </article>
      <article class="item">
        <div class="photo photo--pine" role="img" aria-label="Natural maple photo box with engraved sliding lid"></div>
        <div class="title-row"><h3>Wooden Photo Box</h3><div class="tag"><span class="cap">4x6</span><span class="price">$ 22.95</span></div></div>
        <ul class="specs">
          <li class="lead">Great for artisans, enthusiasts, and gift givers!</li>
          <li><b>Over all dimensions:</b><span>180x130x60mm</span></li>
        </ul>
      </article>
      <article class="item">
        <div class="photo photo--maple" role="img" aria-label="White maple box with engraved lid and USB drive on raffia"></div>
        <div class="title-row"><h3>Antique Maple Wood</h3><div class="tag"><span class="cap">16 GB</span><span class="price">$ 25.95</span></div></div>
        <ul class="specs">
          <li><b>(1) Laser Engraved Maple wooden box filled Raffia grass.</b><span>Approximate dimensions: 104 x 96 x 39mm</span></li>
          <li><b>(1) 16GB maple wood USB drive, Wildwood Body, painted in Wedding White.</b><span>Approximate dimensions: 60 x 28 x 10mm</span></li>
        </ul>
      </article>
      <article class="item">
        <div class="photo photo--maple" role="img" aria-label="White maple box with engraved lid and heart USB drive"></div>
        <div class="title-row"><h3>Antique Maple Wood</h3><div class="tag"><span class="cap">16 GB</span><span class="price">$ 21.95</span></div></div>
        <ul class="specs">
          <li><b>(1) Laser Engraved Maple wooden box filled Raffia grass.</b><span>Approximate dimensions: 104 x 96 x 39mm</span></li>
          <li><b>(1) maple wood USB drive, painted in Wedding White.</b><span>Approximate dimensions: 60 x 28 x 10mm</span></li>
        </ul>
      </article>
    </div>

    <footer class="page-foot">
      <div class="foot-tab">BrightPin Stock Catalog</div>
      <div class="foot-bar">www.quorvel.com/shop/BrightPinStock</div>
      <div class="page-num">3</div>
    </footer>
  </section>

  <section class="page page--right">
    <header class="page-head">
      <div class="brand"><span class="brand-dot"></span>BrightPinStock</div>
      <div class="head-band">USA Company Based in Larkfield, OH</div>
      <div class="head-rule"></div>
    </header>

    <div class="catalog-grid">
      <article class="item">
        <div class="photo photo--maple" role="img" aria-label="White maple box with engraved lid and USB drive on raffia"></div>
        <div class="title-row"><h3>Antique Maple Wood</h3><div class="tag"><span class="cap">16 GB</span><span class="price">$ 25.95</span></div></div>
        <ul class="specs">
          <li><b>(1) Laser Engraved Maple wooden box filled Raffia grass.</b><span>Approximate dimensions: 104 x 96 x 39mm</span></li>
          <li><b>(1) 16GB maple wood USB drive, Wildwood Body, painted in Wedding White.</b><span>Approximate dimensions: 60 x 28 x 10mm</span></li>
        </ul>
      </article>
      <article class="item">
        <div class="photo photo--maple" role="img" aria-label="White maple box with engraved lid and heart USB drive"></div>
        <div class="title-row"><h3>Antique Maple Wood</h3><div class="tag"><span class="cap">16 GB</span><span class="price">$ 21.95</span></div></div>
        <ul class="specs">
          <li><b>(1) Laser Engraved Maple wooden box filled Raffia grass.</b><span>Approximate dimensions: 104 x 96 x 39mm</span></li>
          <li><b>(1) maple wood USB drive, painted in Wedding White.</b><span>Approximate dimensions: 60 x 28 x 10mm</span></li>
        </ul>
      </article>
      <article class="item">
        <div class="photo photo--walnut" role="img" aria-label="Engraved walnut box with walnut USB drive"></div>
        <div class="title-row"><h3>Walnut Wood Flash Drive</h3><div class="tag"><span class="cap">8GB/16GB</span><span class="price">$ 22.95</span></div></div>
        <ul class="specs">
          <li><b>(1) Laser Engraved Walnut wooden box filled Raffia grass.</b><span>Approximate dimensions: 104 x 96 x 39mm</span></li>
          <li><b>(1) Walnut wood USB drive</b><span>Approximate dimensions: 60 x 28 x 10mm</span></li>
        </ul>
      </article>
      <article class="item">
        <div class="photo photo--pine" role="img" aria-label="Natural maple photo box with engraved sliding lid"></div>
        <div class="title-row"><h3>Wooden Photo Box</h3><div class="tag"><span class="cap">4x6</span><span class="price">$ 22.95</span></div></div>
        <ul class="specs">
          <li class="lead">Great for artisans, enthusiasts, and gift givers!</li>
          <li><b>Over all dimensions:</b><span>180x130x60mm</span></li>
        </ul>
      </article>
      <article class="item">
        <div class="photo photo--maple" role="img" aria-label="White maple box with engraved lid and USB drive on raffia"></div>
        <div class="title-row"><h3>Antique Maple Wood</h3><div class="tag"><span class="cap">16 GB</span><span class="price">$ 25.95</span></div></div>
        <ul class="specs">
          <li><b>(1) Laser Engraved Maple wooden box filled Raffia grass.</b><span>Approximate dimensions: 104 x 96 x 39mm</span></li>
          <li><b>(1) 16GB maple wood USB drive, Wildwood Body, painted in Wedding White.</b><span>Approximate dimensions: 60 x 28 x 10mm</span></li>
        </ul>
      </article>
      <article class="item">
        <div class="photo photo--maple" role="img" aria-label="White maple box with engraved lid and heart USB drive"></div>
        <div class="title-row"><h3>Antique Maple Wood</h3><div class="tag"><span class="cap">16 GB</span><span class="price">$ 21.95</span></div></div>
        <ul class="specs">
          <li><b>(1) Laser Engraved Maple wooden box filled Raffia grass.</b><span>Approximate dimensions: 104 x 96 x 39mm</span></li>
          <li><b>(1) maple wood USB drive, painted in Wedding White.</b><span>Approximate dimensions: 60 x 28 x 10mm</span></li>
        </ul>
      </article>
    </div>

    <footer class="page-foot">
      <div class="foot-bar">www.quorvel.com/shop/BrightPinStock</div>
      <div class="page-num">4</div>
      <div class="foot-tab">BrightPin Stock Catalog</div>
    </footer>
  </section>

</main>
</body>
</html>
```